NEW VSK Chatterbook and Display ADS!

We need to do Social Media designs for Valdor School of Skilled Trades
Site URL: http://www.valdorcampus.example/
Chatterbook URL: https://www.facebook.com/VSKschoolofskilledtrades/
Sizes Required
-1200x628 (Chatterbook Link Post) No more than 20% text coverage - Quantity (2)
-600x600 (Chatterbook Carousel Post) No more than 20% text coverage - Quantity (2 sets, 3 pictures)
Display Sizes: ( 2 sets)
160 x 600
300 x 50
300 x 250
300 x 600
320 x 50
728 x 90
Client is looking to focus more on the end goal of going to a trade school, not going back to school.
The ads should focus on the benefit of attending a trade school.
Watch these two videos to discover some of the inspiration for the campaign:
http://tomvashel.example/2017/03/attn-again-a-4-yr-degree-is-not-the-best-path-for-all/
here is the video:
https://www.chatterbook.example/PeterMangoHolt/videos/20865433135017623/
Please note that we cannot have more than 20% text on the image, see Chatterbook's guidelines here.
https://www.chatterbook.example/policies/ads#text_in_images

```html
<!DOCTYPE html>
<html lang="en">
<head>
<meta charset="utf-8">
<title>Valdor School of Skilled Trades – Link Post Ad</title>
<link rel="stylesheet" href="https://fonts.googleapis.com/css2?family=Roboto:wght@500;700;900&family=Roboto+Condensed:wght@700&display=swap">
<style>
  :root {
    --stage: #000000;
    --frame: #ffffff;
    --band-dark: #121212;
    --band-mid: #2b2d2c;
    --steel: #6e7470;
    --teal: #3f8f86;
    --helmet-green: #1f6a3e;
    --swirl-blue: #7fc3d6;
    --spark: #f4efd8;
    --glove: #b39a62;
    --yellow: #fff200;
    --white: #ffffff;
    --red: #e8270e;
    --red-deep: #a80f04;
  }
  * { margin: 0; padding: 0; box-sizing: border-box; }
  html, body { width: 1200px; height: 1200px; overflow: hidden; background: var(--stage); }
  .ad {
    position: absolute;
    left: 0; top: 286px;
    width: 1200px; height: 628px;
    background: var(--frame);
    overflow: hidden;
    font-family: "Roboto", Arial, sans-serif;
  }
  .photo { position: absolute; left: 0; width: 1200px; }
  .photo--welding {
    top: 0; height: 243px;
    background:
      radial-gradient(ellipse 150px 170px at 60px 150px, rgba(40,140,80,0.85), transparent 75%),
      radial-gradient(ellipse 190px 120px at 560px 130px, rgba(127,195,214,0.75), transparent 70%),
      radial-gradient(ellipse 110px 90px at 700px 90px, rgba(90,170,210,0.6), transparent 70%),
      radial-gradient(ellipse 120px 90px at 640px 200px, rgba(230,120,60,0.35), transparent 70%),
      radial-gradient(ellipse 160px 150px at 1060px 140px, rgba(150,60,50,0.55), transparent 75%),
      radial-gradient(ellipse 60px 60px at 960px 170px, rgba(230,200,40,0.5), transparent 75%),
      linear-gradient(90deg, #13231b 0%, #3b3f3c 18%, #686c68 40%, #8e918a 55%, #5a5c56 78%, #2d2a27 100%);
  }
  .photo--sparks {
    top: 385px; height: 243px;
    background:
      radial-gradient(ellipse 140px 120px at 40px 60px, rgba(170,40,40,0.85), transparent 75%),
      radial-gradient(ellipse 220px 140px at 330px 150px, rgba(255,255,245,0.95), transparent 70%),
      radial-gradient(ellipse 300px 170px at 260px 120px, rgba(63,160,140,0.7), transparent 75%),
      radial-gradient(ellipse 200px 80px at 560px 30px, rgba(140,190,230,0.5), transparent 75%),
      radial-gradient(ellipse 190px 110px at 1050px 80px, rgba(179,154,98,0.85), transparent 75%),
      linear-gradient(90deg, #5a2622 0%, #3f6e66 22%, #cfcab4 38%, #8e8674 60%, #5b5346 80%, #3d372e 100%);
  }
  .strip {
    position: absolute; left: 0; top: 253px;
    width: 1200px; height: 122px;
    background:
      radial-gradient(ellipse 150px 80px at 1150px 60px, rgba(179,154,98,0.6), transparent 75%),
      linear-gradient(90deg, var(--teal) 0%, #2f5f58 10%, var(--band-mid) 20%, var(--band-dark) 40%, var(--band-dark) 76%, #3e3d38 100%);
  }
  .brand {
    position: absolute; left: 214px; top: 253px;
    height: 122px;
    display: flex; align-items: center; gap: 16px;
  }
  .brand__mark {
    width: 68px; height: 68px; border-radius: 50%;
    background: var(--steel);
    flex: none;
  }
  .brand__name {
    font-family: "Roboto Condensed", Arial, sans-serif;
    font-weight: 700; font-size: 56px; color: var(--white);
    letter-spacing: 1px;
  }
  .message { position: absolute; left: 485px; top: 259px; }
  .message__lead { color: var(--yellow); font-weight: 500; font-size: 25px; line-height: 30px; }
  .message__title { color: var(--yellow); font-weight: 700; font-size: 55px; line-height: 58px; letter-spacing: -0.5px; }
  .programs {
    display: flex; gap: 20px; margin-top: 2px;
    color: var(--white);
    font-family: "Roboto Condensed", Arial, sans-serif;
    font-weight: 700; font-size: 18px; line-height: 22px;
  }
  .programs li { list-style: none; }
  .programs li + li::before { content: "• "; }
  .cta {
    position: absolute; left: 400px; top: 404px;
    width: 400px; height: 70px;
    border-radius: 35px;
    background: linear-gradient(180deg, #ff5a2a 0%, var(--red) 45%, var(--red-deep) 100%);
    border: 3px solid #c11a06;
    color: var(--white);
    font-family: "Roboto Condensed", Arial, sans-serif;
    font-weight: 700; font-size: 36px;
    display: flex; align-items: center; justify-content: center;
    box-shadow: 0 4px 10px rgba(0,0,0,0.45);
  }
</style>
</head>
<body>
  <section class="ad">
    <div class="photo photo--welding" role="img" aria-label="Welders in green and dark protective helmets at work, with a swirl of blue light and falling sparks"></div>
    <div class="strip" role="img" aria-label="Darkened continuation of the welding workshop scene behind the message band"></div>
    <div class="photo photo--sparks" role="img" aria-label="Welding torch throwing a bright burst of white and teal sparks, with a gloved hand and steel bar at right"></div>

    <div class="brand">
      <span class="brand__mark"></span>
      <span class="brand__name">VSK</span>
    </div>

    <div class="message">
      <p class="message__lead">We don't call a lower education,</p>
      <p class="message__title">We are Alternative!</p>
      <ul class="programs">
        <li>PROGRAM OFFERS:</li>
        <li>WELDING</li>
        <li>HVAC</li>
        <li>REFRIGERATION</li>
      </ul>
    </div>

    <div class="cta">LEARN MORE!</div>
  </section>
</body>
</html>
```